Website Design For Atelier Nine Design Group

Create a sophisticated website that denotes high-end luxury. We would like to keep the copy minimalist and elegantly understated while communicating only the most essential information. While creating an air of exclusivity.
We would like 3-4 Tab Wesbite
Home:
• Feature a design project front and centre, along with a short
introduction about who we are and what we do.

We can put a Call To Action at the end of the introduction inviting readers to learn more on our About page.
About:
• This page should provide more detail on our background, past
achievements, history of the company, and anything you'd like to
highlight.
• We should also provide details on our services, aesthetic, process, etc.
Team:
• introduce the team, possibly with short descriptions for each
team member. Total Team Members 7
Residential
• The portfolio page can be a grid of images along with titles for
each project.
• Clicking on each image should take you to a separate page for that
project where readers can find more details

Commercial
The portfolio page can be a grid of images along with titles for
each project.

Contact Us:

example website:
https://www.venkorahinteriors.example/

Target Market(s)

High end luxury clientele

Industry/Entity Type

Interior Design

Number of Pages Required

4 page

Font styles to use
Sans Serif

Requirements
Must have
• Company logo, color scheme and name: Atelier Nine Design Group

```html
<!DOCTYPE html>
<html lang="en">
<head>
<meta charset="utf-8">
<title>Atelier Nine Design Group</title>
<link href="https://fonts.googleapis.com/css2?family=Red+Hat+Display:wght@400;500&family=Roboto:wght@400;500&display=swap" rel="stylesheet">
<style>
  :root{
    --gold:#c9a24a;
    --navy:#022b3a;
    --navy-soft:#0a3545;
    --ink:#1d1d1d;
    --muted:#6f6f6f;
    --paper:#ffffff;
    --band:#f5f5f5;
    --footer:#e2e2e4;
    --head:"Red Hat Display", sans-serif;
    --body:"Roboto", sans-serif;
  }
  *{margin:0;padding:0;box-sizing:border-box}
  html,body{width:698px;height:1200px;overflow:hidden;background:var(--paper)}
  body{position:relative;font-family:var(--body);color:var(--ink)}
  .abs{position:absolute}

  /* header */
  .site-header{left:0;top:0;width:698px;height:44px;background:var(--paper)}
  .brand{left:16px;top:15px;display:flex;align-items:center;gap:4px}
  .brand-square{width:8px;height:8px;background:var(--gold)}
  .brand-name{font-family:var(--head);font-weight:500;font-size:8px;letter-spacing:.8px;color:var(--navy)}
  .main-nav a{position:absolute;top:18px;font-size:5.8px;color:var(--navy);text-decoration:none;white-space:nowrap}
  .main-nav a.active{color:var(--gold)}

  /* hero */
  .hero{left:0;top:44px;width:698px;height:276px;background:linear-gradient(100deg,#6b4a33 0%,#8a4a2c 30%,#5b3a27 60%,#3b2a20 100%)}
  .hero-shade{left:0;top:44px;width:698px;height:276px;background:rgba(0,0,0,.28)}
  .hero-band{left:0;top:320px;width:698px;height:44px;background:var(--band)}
  .hero-title{left:141px;top:118px;font-family:var(--head);font-weight:400;font-size:32px;line-height:39px;color:#fff;width:240px}
  .hero-text{left:141px;top:204px;width:200px;font-size:7.4px;line-height:12.4px;color:#fff}
  .btn{display:flex;align-items:center;justify-content:center;font-size:5.8px;color:#fff}
  .hero-btn{left:143px;top:262px;width:57px;height:18px;background:var(--gold)}
  .slide-number{left:244px;top:254px;font-family:var(--body);font-weight:400;font-size:106px;line-height:106px;color:rgba(240,240,240,.95);letter-spacing:4px}
  .arrow{top:287px;width:55px;height:55px;display:flex;align-items:center;justify-content:center}
  .arrow-prev{left:567px;background:var(--gold)}
  .arrow-next{left:622px;background:var(--navy)}

  /* about */
  .photo-a{left:142px;top:406px;width:110px;height:127px;background:linear-gradient(160deg,#4a3324,#7a4a2a 55%,#5a2a22)}
  .photo-b{left:224px;top:439px;width:120px;height:160px;background:linear-gradient(170deg,#3a3a3c,#6a6460 50%,#d9d2c6 80%,#4a4a4c)}
  .eyebrow{font-size:5.6px;color:var(--gold);letter-spacing:.2px}
  .about-eyebrow{left:390px;top:440px}
  .about-title{left:390px;top:452px;font-family:var(--head);font-weight:400;font-size:13.4px;line-height:17px;color:var(--ink)}
  .about-lead{left:390px;top:497px;width:180px;font-size:9.4px;line-height:13.3px;color:var(--muted)}
  .about-body{left:390px;top:527px;width:170px;font-size:7.1px;line-height:12.4px;color:var(--muted)}
  .about-btn{left:390px;top:589px;width:58px;height:18px;background:var(--navy)}

  /* newsletter */
  .newsletter{left:0;top:646px;width:698px;height:145px;background:var(--navy)}
  .newsletter-map{left:141px;top:646px;width:414px;height:145px;background:radial-gradient(ellipse at 50% 45%,var(--navy-soft),var(--navy) 70%)}
  .news-eyebrow{left:142px;top:689px}
  .news-title{left:142px;top:701px;font-family:var(--head);font-size:14px;color:#fff}
  .email-field{left:142px;top:734px;width:158px;height:18px;background:#f3f3f3;font-size:5.8px;color:#555;display:flex;align-items:center;padding-left:8px}
  .subscribe-btn{left:308px;top:734px;width:58px;height:18px;background:var(--gold)}
  .feature-photo{left:471px;top:670px;width:201px;height:201px;background:linear-gradient(150deg,#dcdcd8 0%,#1f4a3a 40%,#2a4a3c 55%,#9a9a96 75%,#4a4a48 100%)}

  /* spotlight */
  .spot-eyebrow{left:0;width:692px;top:841px;text-align:center}
  .spot-title{left:0;width:692px;top:853px;text-align:center;font-family:var(--head);font-size:14.3px;color:var(--ink)}
  .spot-text{left:248px;top:881px;width:200px;text-align:center;font-size:7.2px;line-height:12.4px;color:var(--muted)}
  .feed-tile{top:925px;width:131px;height:175px}
  .dot{top:1114px;height:1px}

  /* footer */
  .site-footer{left:0;top:1137px;width:698px;height:63px;background:var(--footer)}
  .legal{left:0;width:698px;top:1159px;text-align:center;font-size:4.8px;letter-spacing:.5px;color:#7a7a7a}
  .social{top:1175px;width:9px;height:9px;border-radius:50%;background:#7a7a7a}
</style>
</head>
<body>
  <header class="abs site-header">
    <div class="abs brand"><span class="brand-square"></span><span class="brand-name">ATELIER NINE</span></div>
    <nav class="main-nav">
      <a class="active" style="left:141px">Home</a>
      <a style="left:176px">About</a>
      <a style="left:210px">Team</a>
      <a style="left:242px">Residential</a>
      <a style="left:289px">Commercial</a>
      <a style="left:339px">Contact Us</a>
    </nav>
  </header>

  <section>
    <div class="abs hero" role="img" aria-label="Interior detail with rust and tan cushions against a stone wall"></div>
    <div class="abs hero-shade"></div>
    <div class="abs hero-band"></div>
    <h1 class="abs hero-title">Creative Web Design Studio</h1>
    <p class="abs hero-text">Lorem ipsum dolor sit amet, consectetur adipiscing elit. Ut eleifend efficitur quam, eu congue odio tristique eu. Cras eu elit justo. Cras efficitur nisi augue.</p>
    <a class="abs btn hero-btn">Learn more</a>
    <div class="abs slide-number">01</div>
    <div class="abs arrow arrow-prev"><svg width="12" height="8" viewBox="0 0 12 8"><path d="M11 4H1M4 1L1 4l3 3" stroke="#fff" stroke-width="1" fill="none"/></svg></div>
    <div class="abs arrow arrow-next"><svg width="12" height="8" viewBox="0 0 12 8"><path d="M1 4h10M8 1l3 3-3 3" stroke="#fff" stroke-width="1" fill="none"/></svg></div>
  </section>

  <section>
    <div class="abs photo-a" role="img" aria-label="Warm wood-panelled bedroom with antique trunk"></div>
    <div class="abs photo-b" role="img" aria-label="Designer reviewing a large material sample book at an event"></div>
    <p class="abs eyebrow about-eyebrow">ABOUT US</p>
    <h2 class="abs about-title">We are the Creative<br>Digital Team</h2>
    <p class="abs about-lead">Suspendisse sit amet facilisis massa. Aliquam egestas.</p>
    <p class="abs about-body">Mauris id faucibus eros. Pellentesque semper venenatis est, ut luctus elit maximus vitae. Mauris lectus tortor, dictum sed dapibus sit amet, tempor sit amet velit. Sed consectetur ex nec ornare.</p>
    <a class="abs btn about-btn">Learn more</a>
  </section>

  <section>
    <div class="abs newsletter"></div>
    <div class="abs newsletter-map" role="img" aria-label="Faint dotted world map"></div>
    <p class="abs eyebrow news-eyebrow">NEWSLETTER</p>
    <h2 class="abs news-title">Want to get updates?</h2>
    <div class="abs email-field">Enter Your Email Address</div>
    <a class="abs btn subscribe-btn">Subscribe</a>
    <div class="abs feature-photo" role="img" aria-label="Lounge with green upholstered wall panels and grey armchairs"></div>
  </section>

  <section>
    <p class="abs eyebrow spot-eyebrow">SPOTLIGHT</p>
    <h2 class="abs spot-title">Atelier Nine Design Group</h2>
    <p class="abs spot-text">To see what we're up to each day follow us on Pictogrid and check out our stories</p>
    <div class="abs feed-tile" style="left:0;background:linear-gradient(135deg,#e8d8c4,#6a5a4a)" role="img" aria-label="Sepia portrait artwork"></div>
    <div class="abs feed-tile" style="left:141.5px;background:linear-gradient(90deg,#4a6a8a,#1f3a5a 35%,#cfd2d4 60%,#e4e4e4)" role="img" aria-label="Blurred doorway video still"></div>
    <div class="abs feed-tile" style="left:283px;background:linear-gradient(180deg,#e4e2de,#7a746c 55%,#2a2624)" role="img" aria-label="Designer seated in a kitchen"></div>
    <div class="abs feed-tile" style="left:425px;background:linear-gradient(180deg,#5a5a54,#d8d8d4 40%,#c8a878 90%)" role="img" aria-label="Cafe with black pendant lamps"></div>
    <div class="abs feed-tile" style="left:566.5px;background:linear-gradient(180deg,#cfc9c0,#3a3230 55%,#1e1c1c)" role="img" aria-label="Two team members in leather outfits"></div>
    <div class="abs dot" style="left:327px;width:13px;background:var(--gold)"></div>
    <div class="abs dot" style="left:345px;width:8px;background:#c8c8c8"></div>
    <div class="abs dot" style="left:358px;width:7px;background:#c8c8c8"></div>
  </section>

  <footer class="abs site-footer"></footer>
  <p class="abs legal">© COPYRIGHT 2022 ATELIER NINE DESIGN STUDIO ALL RIGHTS RESERVED. | PRIVACY | SITEMAP</p>
  <span class="abs social" style="left:332px"></span>
  <span class="abs social" style="left:347px"></span>
  <span class="abs social" style="left:361px"></span>
</body>
</html>
```